LEARN Business Skills so you can Earn a good living

size of the poster is 8”x 10.75" plus 0.25" bleed.
Please leave 1 inch on the bottoum for footer
I want a design a poster that will attract people's attention.
I appreciate a creative ad however the ad should not take away from being able to clearly read the text.
-I also appreciate a simple creative ad that is not too busy.
-you can use graphics, vectors, or pictures of real people.
-however, if you use real people it should be a white male that is wearing a white shirt and look like a professional person.

Target Market(s)

Potential young business people

Industry/Entity Type

education

Requirements
Must have
• easy to read the text
Nice to have
• I would like a "creative" simple ad that is easy to be read
Should not have
• pictures of women

```html
<!DOCTYPE html>
<html lang="en">
<head>
<meta charset="utf-8">
<title>Business Enrichment Course Poster</title>
<link href="https://fonts.googleapis.com/css2?family=Roboto:wght@400;500;700;900&family=Roboto+Condensed:wght@400;700&family=Bebas+Neue&display=swap" rel="stylesheet">
<style>
  :root {
    --page-bg: #d9d9d9;
    --navy-deep: #132f63;
    --navy-mid: #1a4a94;
    --navy-glow: #2463b8;
    --sky: #29abe2;
    --pale-blue: #8fb8e6;
    --white: #ffffff;
    --list-text: #e8eef8;
  }
  * { margin: 0; padding: 0; box-sizing: border-box; }
  html, body {
    width: 976px; height: 1200px; overflow: hidden;
    background: var(--page-bg);
  }
  .poster {
    position: absolute; left: 38px; top: 10px;
    width: 900px; height: 1180px; overflow: hidden;
    background: radial-gradient(ellipse 60% 45% at 55% 42%, var(--navy-glow) 0%, var(--navy-mid) 45%, var(--navy-deep) 100%);
    color: var(--white);
    font-family: "Roboto", Arial, sans-serif;
  }
  .top-band {
    position: absolute; left: 0; top: 34px; width: 100%; height: 50px;
    background: var(--sky);
    display: flex; align-items: center; justify-content: center;
    font-family: "Roboto Condensed", Arial, sans-serif;
    font-size: 28px; letter-spacing: 1px; font-weight: 400;
  }
  .top-band strong { font-weight: 700; }
  .title {
    position: absolute; left: 0; top: 122px; width: 100%;
    text-align: center; font-weight: 700; font-size: 63px; line-height: 68px;
    letter-spacing: 1px;
  }
  .tagline {
    position: absolute; left: 0; top: 280px; width: 100%;
    text-align: center; font-size: 21px; font-weight: 400;
  }
  .slogan {
    position: absolute; left: 46px; top: 400px; width: 300px;
    text-align: center; color: var(--pale-blue);
    font-family: "Roboto Condensed", Arial, sans-serif; font-weight: 700;
  }
  .slogan-line { font-size: 76px; line-height: 82px; letter-spacing: 1px; }
  .slogan-joiner {
    display: flex; align-items: center; justify-content: center; gap: 14px;
    font-family: "Roboto", Arial, sans-serif; font-weight: 500;
    font-size: 38px; line-height: 52px;
  }
  .joiner-rule { display: block; }
  .illustration {
    position: absolute; left: 435px; top: 313px; width: 420px; height: 465px;
  }
  .skills-band {
    position: absolute; left: 0; top: 738px; width: 381px; height: 51px;
  }
  .skills-band-shape { position: absolute; left: 0; top: 0; width: 381px; height: 51px; }
  .skills-band-label {
    position: absolute; left: 38px; top: 0; height: 51px;
    display: flex; align-items: center;
    font-family: "Bebas Neue", "Roboto Condensed", sans-serif;
    font-size: 27px; letter-spacing: 0.5px; white-space: nowrap;
  }
  .benefits {
    position: absolute; left: 0; top: 818px; width: 100%;
  }
  .benefit {
    position: absolute; width: 220px; text-align: center;
    font-size: 23px; line-height: 29px;
  }
  .benefit svg { display: block; margin: 0 auto 18px; }
  .benefit-job { left: 114px; }
  .benefit-business { left: 328px; }
  .benefit-salary { left: 543px; }
  .course-list {
    position: absolute; left: 20px; top: 1030px; width: 860px;
    text-align: center; color: var(--list-text);
    font-family: "Roboto Condensed", Arial, sans-serif; font-weight: 400;
    font-size: 14px; line-height: 22px; text-transform: uppercase;
    letter-spacing: -0.2px;
  }
  .course-line { display: block; white-space: nowrap; }
  .course-list strong { font-weight: 700; }
</style>
</head>
<body>
<main class="poster">
  <div class="top-band"><span><strong>LEARN</strong> BUSINESS <strong>SKILLS</strong> SO YOU CAN <strong>EARN</strong> A GOOD LIVING</span></div>

  <h1 class="title">BUSINESS<br>ENRICHMENT COURSE</h1>
  <p class="tagline">A proven success of helping people in their livelihoods</p>

  <div class="slogan">
    <div class="slogan-line">LEARN IT</div>
    <div class="slogan-joiner">
      <svg class="joiner-rule" width="92" height="10" aria-hidden="true"><line x1="5" y1="5" x2="87" y2="5" stroke="#ffffff" stroke-width="2"/><circle cx="5" cy="5" r="4" fill="#ffffff"/><circle cx="87" cy="5" r="4" fill="#ffffff"/></svg>
      <span>to</span>
      <svg class="joiner-rule" width="92" height="10" aria-hidden="true"><line x1="5" y1="5" x2="87" y2="5" stroke="#ffffff" stroke-width="2"/><circle cx="5" cy="5" r="4" fill="#ffffff"/><circle cx="87" cy="5" r="4" fill="#ffffff"/></svg>
    </div>
    <div class="slogan-line">EARN IT</div>
  </div>

  <svg class="illustration" viewBox="0 0 420 465" role="img" aria-label="Illustration of businessmen with a large magnifying glass, a question mark, gears, a flip chart and a desk with a laptop">
    <defs>
      <radialGradient id="illus-tone" cx="50%" cy="45%" r="60%">
        <stop offset="0%" stop-color="#6f9fd8" stop-opacity="0.55"/>
        <stop offset="100%" stop-color="#2a5fae" stop-opacity="0"/>
      </radialGradient>
    </defs>
    <rect width="420" height="465" fill="url(#illus-tone)"/>
  </svg>

  <div class="skills-band">
    <svg class="skills-band-shape" viewBox="0 0 381 51" aria-hidden="true">
      <polygon points="0,0 381,0 358,51 0,51" fill="#29abe2"/>
    </svg>
    <div class="skills-band-label">BUSINESS SKILLS THAT WILL HELP YOU:</div>
  </div>

  <section class="benefits">
    <div class="benefit benefit-job">
      <svg width="100" height="100" viewBox="0 0 100 100" aria-hidden="true">
        <circle cx="50" cy="50" r="48" fill="none" stroke="#29abe2" stroke-width="1.5" stroke-dasharray="2 3"/>
        <circle cx="50" cy="34" r="11" fill="none" stroke="#fff" stroke-width="2.5"/>
        <text x="50" y="40" text-anchor="middle" font-family="Roboto, sans-serif" font-size="15" font-weight="700" fill="#fff">$</text>
        <path d="M22 62 h12 l10 -5 h16 a4 4 0 0 1 0 8 h-12 M48 65 h20 l12 -9 a4 4 0 0 1 5 6 l-14 12 h-37" fill="none" stroke="#fff" stroke-width="2.5" stroke-linejoin="round" stroke-linecap="round"/>
      </svg>
      Get a<br>quality job
    </div>
    <div class="benefit benefit-business">
      <svg width="100" height="100" viewBox="0 0 100 100" aria-hidden="true">
        <circle cx="50" cy="50" r="48" fill="none" stroke="#29abe2" stroke-width="1.5" stroke-dasharray="2 3"/>
        <rect x="56" y="42" width="7" height="26" fill="#fff"/>
        <rect x="67" y="32" width="7" height="36" fill="#fff"/>
        <path d="M24 56 l14 -12 l10 8 l22 -24" fill="none" stroke="#fff" stroke-width="2.5" stroke-linecap="round"/>
        <path d="M64 27 h7 v7" fill="none" stroke="#fff" stroke-width="2.5" stroke-linecap="round"/>
        <circle cx="40" cy="62" r="9" fill="none" stroke="#fff" stroke-width="2.5"/>
        <line x1="34" y1="69" x2="26" y2="78" stroke="#fff" stroke-width="3.5" stroke-linecap="round"/>
      </svg>
      Start/grow<br>your business
    </div>
    <div class="benefit benefit-salary">
      <svg width="100" height="100" viewBox="0 0 100 100" aria-hidden="true">
        <circle cx="50" cy="50" r="48" fill="none" stroke="#29abe2" stroke-width="1.5" stroke-dasharray="2 3"/>
        <rect x="34" y="28" width="44" height="24" rx="2" fill="none" stroke="#fff" stroke-width="2.5"/>
        <circle cx="56" cy="40" r="7" fill="none" stroke="#fff" stroke-width="2"/>
        <text x="56" y="44.5" text-anchor="middle" font-family="Roboto, sans-serif" font-size="10" font-weight="700" fill="#fff">$</text>
        <path d="M22 58 v18 M22 60 h10 l10 6 h12 a4 4 0 0 1 0 8 h-16" fill="none" stroke="#fff" stroke-width="2.5" stroke-linecap="round" stroke-linejoin="round"/>
      </svg>
      Increase<br>your salary
    </div>
  </section>

  <p class="course-list">
    <span class="course-line">Business Administration - <strong>Small Business Management</strong> - Finance - <strong>Investments</strong> - Computers - <strong>Accounting</strong> - Sales Marketing - <strong>Project</strong></span>
    <span class="course-line"><strong>Management Interviewing Skills</strong> - Business Law - <strong>Negotiation</strong> – Public Speaking - <strong>Import/Export</strong> - Information Technology - <strong>Distribution</strong></span>
    <span class="course-line">Marketing - <strong>LedgerBooks</strong> - Real Estate - <strong>Health Care</strong> - Management - <strong>ShopRiver</strong></span>
  </p>
</main>
</body>
</html>
```